Project Lists Banner for HVAC ecommerce store

We want a banner that showcases our project list feature that will allow customers to create list of products that they can select and quickly order. this will be a middle of page banner. It will replace this banner - https://www.glimmerpanecapture.com/image/48305712
Font: Noto Sans
Size: 938x300 px
Color Options: #0059E, #00BBE3, #C6C8C7
Text:
Create lists of frequently purchased SKU's for fast ordering.
- Warehouse Inventory
- Complete Systems
- Large Projects
- And More...
"Sign In" is the call to action button. make button with non rounded (square) boarders.
We don't want a computer screen in banner nor a person. You can look at our competitors below for ideas.
Our staging server is plumvale7.com for reference
Our competitors:
https://www.brightfolddepot.com/
https://www.tolvexa.com/
https://www.plosk.com/
https://www.vimbo.com/index.html
HVAC, B2B
HVAC

```html
<!DOCTYPE html>
<html lang="en">
<head>
<meta charset="utf-8">
<title>Project Lists Banner</title>
<link href="https://fonts.googleapis.com/css2?family=Noto+Sans:wght@400;700&display=swap" rel="stylesheet">
<style>
  :root {
    --page-bg: #ffffff;
    --banner-deep: #174a80;
    --banner-mid: #2d5a8a;
    --banner-haze: #6c7f96;
    --haze-warm: rgba(160, 150, 130, 0.35);
    --accent-cyan: #1fb4e2;
    --text-white: #ffffff;
  }
  * { box-sizing: border-box; margin: 0; padding: 0; }
  html, body {
    width: 1200px;
    height: 604px;
    overflow: hidden;
    background: var(--page-bg);
    font-family: "Noto Sans", sans-serif;
  }
  .canvas {
    position: relative;
    width: 1200px;
    height: 604px;
  }
  .banner {
    position: absolute;
    left: 50px;
    top: 121px;
    width: 1102px;
    height: 351px;
    overflow: hidden;
    background: linear-gradient(90deg, var(--banner-deep) 0%, var(--banner-deep) 36%, var(--banner-mid) 58%, var(--banner-haze) 100%);
    box-shadow: 0 3px 8px rgba(0, 0, 0, 0.35);
  }
  .cart-photo {
    position: absolute;
    left: 400px;
    top: 0;
    width: 360px;
    height: 351px;
    background:
      radial-gradient(ellipse 45% 30% at 45% 18%, var(--haze-warm) 0%, rgba(160, 150, 130, 0) 100%),
      radial-gradient(ellipse 55% 45% at 45% 62%, rgba(120, 135, 155, 0.35) 0%, rgba(40, 80, 130, 0) 100%);
  }
  .floor-glow {
    position: absolute;
    left: 380px;
    top: 250px;
    width: 722px;
    height: 101px;
    background: linear-gradient(180deg, rgba(110, 130, 155, 0) 0%, rgba(110, 130, 155, 0.35) 100%);
  }
  .product-group {
    position: absolute;
    left: 0;
    top: 0;
    width: 1102px;
    height: 351px;
  }
  .copy {
    position: absolute;
    left: 32px;
    top: 24px;
    color: var(--text-white);
  }
  .headline {
    font-weight: 700;
    font-size: 37.5px;
    line-height: 45px;
    letter-spacing: 0;
    white-space: nowrap;
  }
  .feature-list {
    list-style: none;
    margin-top: 21px;
  }
  .feature-list li {
    display: flex;
    align-items: center;
    height: 43px;
    font-size: 30.5px;
    font-weight: 400;
    white-space: nowrap;
  }
  .feature-list svg {
    width: 22px;
    height: 22px;
    margin-left: 1px;
    margin-right: 23px;
    flex: none;
  }
  .sign-in {
    display: block;
    margin-top: 10px;
    margin-left: 1px;
    width: 183px;
    height: 41px;
    background: var(--accent-cyan);
    color: var(--text-white);
    font-weight: 700;
    font-size: 27px;
    line-height: 41px;
    text-align: center;
    text-decoration: none;
    border-radius: 0;
  }
</style>
</head>
<body>
<div class="canvas">
  <section class="banner">
    <div class="cart-photo" role="img" aria-label="Faded photo of a shopping cart in a warehouse"></div>
    <div class="floor-glow"></div>

    <svg class="product-group" viewBox="0 0 1102 351" role="img" aria-label="Photo of a tan gas furnace, a tan outdoor condenser unit and a white touchscreen thermostat">
      <defs>
        <linearGradient id="furnace-side" x1="0" x2="1">
          <stop offset="0" stop-color="#8f7a62"/>
          <stop offset="1" stop-color="#a8927a"/>
        </linearGradient>
        <linearGradient id="furnace-front" x1="0" y1="0" x2="1" y2="1">
          <stop offset="0" stop-color="#c2ab8f"/>
          <stop offset="0.6" stop-color="#b59e83"/>
          <stop offset="1" stop-color="#a38c72"/>
        </linearGradient>
        <linearGradient id="condenser-side" x1="0" x2="1">
          <stop offset="0" stop-color="#9b8670"/>
          <stop offset="1" stop-color="#b29c83"/>
        </linearGradient>
        <linearGradient id="condenser-front" x1="0" y1="0" x2="1" y2="1">
          <stop offset="0" stop-color="#c8b398"/>
          <stop offset="0.5" stop-color="#bba488"/>
          <stop offset="1" stop-color="#a99378"/>
        </linearGradient>
        <linearGradient id="thermo-body" x1="0" y1="0" x2="0" y2="1">
          <stop offset="0" stop-color="#f6f7f8"/>
          <stop offset="1" stop-color="#dfe2e5"/>
        </linearGradient>
        <filter id="soft-shadow" x="-20%" y="-20%" width="140%" height="140%">
          <feGaussianBlur stdDeviation="6"/>
        </filter>
      </defs>

      <ellipse cx="770" cy="322" rx="105" ry="10" fill="rgba(10,25,45,0.45)" filter="url(#soft-shadow)"/>
      <ellipse cx="975" cy="342" rx="150" ry="10" fill="rgba(10,25,45,0.45)" filter="url(#soft-shadow)"/>

      <polygon points="672,44 708,14 708,320 672,306" fill="url(#furnace-side)"/>
      <polygon points="708,14 850,12 850,318 708,320" fill="url(#furnace-front)"/>
      <polygon points="672,44 708,14 850,12 820,40" fill="#cbb69c" opacity="0.55"/>

      <polygon points="832,64 862,38 862,340 832,326" fill="url(#condenser-side)"/>
      <polygon points="862,38 1102,36 1102,340 862,340" fill="url(#condenser-front)"/>

      <ellipse cx="828" cy="349" rx="70" ry="6" fill="rgba(10,25,45,0.4)" filter="url(#soft-shadow)"/>
      <rect x="762" y="260" width="134" height="87" rx="7" fill="url(#thermo-body)"/>
    </svg>

    <div class="copy">
      <h1 class="headline">Create lists of frequently<br>purchased SKU's for fast ordering.</h1>
      <ul class="feature-list">
        <li>
          <svg viewBox="0 0 22 22" aria-hidden="true"><circle cx="11" cy="11" r="11" fill="#1fb4e2"/><path d="M6 11.5l3.3 3.2L16 8" fill="none" stroke="#fff" stroke-width="2.6" stroke-linecap="round" stroke-linejoin="round"/></svg>
          Warehouse Inventory
        </li>
        <li>
          <svg viewBox="0 0 22 22" aria-hidden="true"><circle cx="11" cy="11" r="11" fill="#1fb4e2"/><path d="M6 11.5l3.3 3.2L16 8" fill="none" stroke="#fff" stroke-width="2.6" stroke-linecap="round" stroke-linejoin="round"/></svg>
          Complete Systems
        </li>
        <li>
          <svg viewBox="0 0 22 22" aria-hidden="true"><circle cx="11" cy="11" r="11" fill="#1fb4e2"/><path d="M6 11.5l3.3 3.2L16 8" fill="none" stroke="#fff" stroke-width="2.6" stroke-linecap="round" stroke-linejoin="round"/></svg>
          Large Projects And More...
        </li>
      </ul>
      <a class="sign-in" href="#">SIGN IN</a>
    </div>
  </section>
</div>
</body>
</html>
```